Business Card Design/Stationary Design

We would like designers to submit cool, hip business card designs (plus stationary designs) for a new, upstart software development company located in Toronto.
If you have any questions, please email us.
For inspiration on designs:
http://cardmuse.example/cool-business-cards/
http://layoutnotes.example/2008/05/36-cool-business-cards-you-should%E2%80%99ve-seen.html
http://gigharbor.example/general/18-smokin-hot-business-card-designs/

Card info:

Selvakumar (Selv) Nadarasan

Founder and CEO

47 Brindle Court, Suite 311

Toronto, ON M4K 2T8

Phone: 647-512-7730

Mobile: 416-273-5094

Fax: 647-512-7731

Email: selvakumar.nadarasan@mailbrook.example

www.quendrix.example
Updates

Hi everyone,

In terms of all the designs I have seen so far, here is what I like:

1.  I really like the "back" part of this design.  The "front" looks pretty decent as well, but for the "front", look at #2 on this list.  I like that.

http://www.pitchboard.example/image.aspx?imageLocation=1000_10001_2000_image.jpg&type=design300px&whiteLabelCustId=9999

2. "Side 1" of this I like, the front needs to be reworked.

http://www.pitchboard.example/image.aspx?imageLocation=1000_10002_2000_image.png&type=design300px&whiteLabelCustId=9999

3. http://www.pitchboard.example/image.aspx?imageLocation=1000_10003_2000_image.jpg&type=design300px&whiteLabelCustId=9999

4. http://www.pitchboard.example/image.aspx?imageLocation=1000_10004_2000_image.jpg&type=design300px&whiteLabelCustId=9999

Target Market(s)

We are focused on enterprise customers right now, so businesses with a long-term goal of also reaching out to the consumer market as well.

Industry/Entity Type

Software

Requirements
Must have
• Must look cool, ultra-modern, clean and eye-catching. Must incorporate our logo and the colors found in the logo.

```html
<!DOCTYPE html>
<html lang="en">
<head>
<meta charset="utf-8">
<title>Quendrix Stationery</title>
<link rel="stylesheet" href="https://fonts.googleapis.com/css2?family=Cormorant+Garamond:wght@500&family=Montserrat:wght@400;500;600;700&family=Roboto+Condensed:wght@400&display=swap">
<style>
  :root {
    --ink: #111;
    --label: #8a8a8a;
    --brand-green: #22ee22;
    --vine-light: #e6f7a0;
    --vine-mid: #b8ea8e;
    --vine-mint: #a8f0c8;
    --paper: #fff;
  }
  * { margin: 0; padding: 0; box-sizing: border-box; }
  html, body { width: 1200px; height: 604px; overflow: hidden; background: var(--paper); }
  .canvas { position: relative; width: 1200px; height: 604px; color: var(--ink); }
  address { font-style: normal; }

  .sheet-label {
    position: absolute;
    font-family: "Roboto Condensed", sans-serif;
    color: var(--label);
  }
  .sheet-label--letterhead { left: 10px; top: 0; font-size: 12px; }
  .sheet-label--envelope { left: 537px; top: 258px; font-size: 18px; }

  /* Letterhead */
  .letterhead {
    position: absolute; left: 1px; top: 23px; width: 471px; height: 580px;
    border: 1.5px solid var(--ink); background: var(--paper); overflow: hidden;
  }
  .brand { position: absolute; display: flex; align-items: center; gap: 6px; font-family: "Montserrat", sans-serif; font-weight: 700; color: var(--ink); white-space: nowrap; }
  .brand__dot { border-radius: 50%; background: var(--brand-green); }
  .letterhead .brand { left: 8px; top: 16px; font-size: 22px; }
  .letterhead .brand__dot { width: 18px; height: 18px; }

  .letterhead__contact {
    position: absolute; right: 6px; top: 31px; text-align: right; white-space: nowrap;
    font-family: "Roboto Condensed", sans-serif; font-size: 7.5px; line-height: 11.5px;
  }
  .vine-band {
    position: absolute; height: 14px; border-radius: 7px;
    background: linear-gradient(90deg, var(--vine-mid), var(--vine-light) 40%, var(--vine-mid) 70%, var(--vine-mint));
  }
  .letterhead .vine-band { left: 55px; top: 56px; width: 416px; }

  .letter {
    position: absolute; left: 54px; top: 99px;
    font-family: "Cormorant Garamond", serif; font-weight: 500; font-size: 14px; line-height: 17.1px;
    white-space: nowrap;
    transform: scaleX(0.84); transform-origin: left top;
  }
  .letter .gap { margin-top: 17.1px; }

  .letterhead__signature {
    position: absolute; left: 54px; top: 540px; width: 350px;
    font-family: "Montserrat", sans-serif; font-weight: 600; line-height: 17.5px; white-space: nowrap;
  }
  .letterhead__signature .role-line { text-align: center; font-size: 10.5px; }
  .letterhead__signature .web-line { display: flex; justify-content: space-between; font-size: 9.2px; }

  /* Envelope */
  .envelope {
    position: absolute; left: 531px; top: 292px; width: 667px; height: 289px;
    border: 3.5px solid var(--ink); background: var(--paper); overflow: hidden;
  }
  .envelope__return {
    position: absolute; left: 9px; top: 10px; white-space: nowrap;
    font-family: "Montserrat", sans-serif; font-size: 11.5px; line-height: 15.5px; letter-spacing: 0.3px;
  }
  .envelope__stamp {
    position: absolute; right: 10px; top: 8px; width: 59px; height: 56px;
    background: var(--ink); padding: 7px;
  }
  .envelope__stamp span { display: block; width: 100%; height: 100%; background: var(--brand-green); }
  .envelope__recipient {
    position: absolute; left: 200px; top: 117px; width: 236px; text-align: center; white-space: nowrap;
    font-family: "Montserrat", sans-serif; font-size: 16.5px; line-height: 22px; letter-spacing: 0.3px;
  }
  .envelope .brand { left: 12px; top: 219px; font-size: 34px; }
  .envelope .brand__dot { width: 26px; height: 26px; }
  .envelope .vine-band { left: 5px; top: 260px; width: 512px; }
</style>
</head>
<body>
<main class="canvas">
  <p class="sheet-label sheet-label--letterhead">Stationary: Letterhead</p>

  <section class="letterhead">
    <div class="brand"><span class="brand__dot"></span><span class="brand__name">Quendrix</span></div>
    <address class="letterhead__contact">
      47 Brindle Court, Suite 311&nbsp; Toronto, ON M4K 2T8<br>
      Phone: 647-512-7730&nbsp; Mobile: 416-273-5094&nbsp; Fax: 647-512-7731
    </address>
    <div class="vine-band" role="img" aria-label="Decorative green vine band"></div>

    <article class="letter">
      <p>August 15, 2009<br>Recipient’s Name<br>Street Address<br>City, State, Zip</p>
      <p class="gap">Salutation,<br>
      Lorem ipsum dolor sit amet, consectetuer adipiscing elit. Nam eu nulla. Donec<br>
      lobortis purus vel urna. Nunc laoreet lacinia nunc. In volutpat sodales ipsum.<br>
      Sed vestibulum. Integer in ante. Sed posuere ligula rhoncus erat. Fusce urna dui,<br>
      sollicitudin ac, pulvinar quis, tincidunt et, risus. Quisque a nunc eget nibh<br>
      interdum fringilla. Fusce dapibus odio in est. Nunc egestas mauris ac leo. Nullam<br>
      orci.<br>
      Morbi volutpat leo in ligula. Integer vel magna. Quisque ut magna et nisi<br>
      bibendum sagittis. Fusce elit ligula, sodales sit amet, tincidunt in, ullamcorper<br>
      condimentum, lectus. Aliquam ut massa.&nbsp; Nunc dapibus, nisi et iaculis feugiat,<br>
      leo ipsum venenatis enim, a nonummy magna ante vitae diam. Proin sapien.<br>
      Duis eleifend. Praesent tempor velit molestie neque. Lorem ipsum dolor sit<br>
      amet, consectetuer adipiscing elit. Sed mollis justo eget augue. Donec tempus,<br>
      urna a congue ultrices, lacus magna convallis nulla, non ultrices metus justo et<br>
      purus.<br>
      Sincerely,<br>
      Your Name Here</p>
    </article>

    <footer class="letterhead__signature">
      <p class="role-line">Selvakumar (Selv) Nadarasan ~ Founder &amp; CEO</p>
      <p class="web-line"><span>selvakumar.nadarasan@mailbrook.example</span><span>www.quendrix.example</span></p>
    </footer>
  </section>

  <p class="sheet-label sheet-label--envelope">Stationary: Envelope</p>

  <section class="envelope">
    <address class="envelope__return">
      Quendrix Technologies Inc.<br>47 Brindle Court, Suite 311<br>Toronto, ON M4K 2T8
    </address>
    <div class="envelope__stamp"><span></span></div>
    <address class="envelope__recipient">R. Ashcombe<br>2786 Calder Ave<br>Smyrna, DE 19072</address>
    <div class="brand"><span class="brand__dot"></span><span class="brand__name">Quendrix</span></div>
    <div class="vine-band" role="img" aria-label="Decorative green vine band"></div>
  </section>
</main>
</body>
</html>
```